Flat Belly Design Graphics for Social

I want to create 9 social media graphics (new Instagram size 4:5 (1080 x 1350 pixels) focusing on our Flat Belly Graphics, using the pics attached. Use the attached pics, NO RANDOM STOCK PHOTOGRAPHY. For the color scheme of the graphics, the color palette is attached. YOU MUST POST ALL 9 GRAPHICS IN ONE ENTRY.
Using the 3 titles below, create one set of graphics. 1) with all text, then for the others, use the pictures as detailed below in IMPORTANT:
1. 21-Night Lean Middle Reboot Beyond 50
2. The 20-Second Trim-Core Menu Guide
3. Starlet Tricks to a Slender Midline Beyond 50 - Zero Scalpel Needed
IMPORTANT:
Only use RK Pic 1 and RK Pic 2 with the title, 21-Night Lean Middle Reboot Beyond 50
Only use meal plan1 and meal plan2 pics with the title, 20-Second Trim-Core Menu Guide
Only use starlet tricks 1 and starlet tricks 2 pics with the title, Starlet Tricks to a Slender Midline Beyond 50 - Zero Scalpel Needed
women over 40

```html
<!DOCTYPE html>
<html lang="en">
<head>
<meta charset="utf-8">
<title>Lean Middle Social Graphics Set</title>
<link rel="stylesheet" href="https://fonts.googleapis.com/css2?family=Montserrat:wght@600;700;800;900&family=Allura&display=swap">
<style>
:root{
  --page:#f8eef0;
  --blush:#f7e8ec;
  --rose:#d899ad;
  --rose-deep:#cf8aa1;
  --forest:#364a48;
  --white:#ffffff;
  --photo-warm-a:#6b4a3a;
  --photo-warm-b:#c9a48e;
  --photo-food-a:#4a3428;
  --photo-food-b:#8a6a4c;
  --photo-sky:#6cc4d9;
}
*{box-sizing:border-box;margin:0;padding:0}
html,body{width:945px;height:1200px;overflow:hidden;background:var(--page)}
body{position:relative;font-family:"Montserrat",sans-serif}
.backdrop{position:absolute;inset:0}
.card{position:absolute;width:220px;height:275px;overflow:hidden;box-shadow:0 1px 4px rgba(0,0,0,.12)}
.col-1{left:112px}.col-2{left:362px}.col-3{left:614px}
.row-1{top:138px}.row-2{top:443px}.row-3{top:767px}
.card svg.shapes{position:absolute;inset:0}
.photo{position:absolute}
.t{position:absolute;font-weight:800;line-height:1;white-space:nowrap}
.script{font-family:"Allura",cursive;font-weight:400}
.forest{color:var(--forest)}.rose{color:var(--rose)}.white{color:var(--white)}
.center{left:0;right:0;text-align:center}
.badge{position:absolute;border-radius:50%;background:var(--forest);display:flex;flex-direction:column;align-items:center;justify-content:center;color:var(--white);text-align:center}
</style>
</head>
<body>

<svg class="backdrop" width="945" height="1200" viewBox="0 0 945 1200" aria-hidden="true">
  <path d="M0 260 C200 150 420 190 600 260 C780 330 900 420 945 520 L945 0 L0 0Z" fill="#f8eef0"/>
  <path d="M0 260 C250 160 520 180 945 420 L945 1200 L0 1200Z" fill="#ffffff" opacity=".7"/>
  <path d="M0 690 C200 640 380 760 520 1200 L0 1200Z" fill="#f8eef0"/>
  <path d="M0 385 C120 300 300 240 560 225 C700 220 820 290 945 425" fill="none" stroke="var(--rose)" stroke-width="1"/>
  <path d="M0 790 C80 805 150 820 230 840" fill="none" stroke="var(--rose)" stroke-width="1"/>
  <path d="M302 1040 C290 1100 275 1150 260 1200" fill="none" stroke="var(--rose)" stroke-width="1"/>
  <path d="M945 1040 C900 1110 860 1160 830 1200" fill="none" stroke="var(--rose)" stroke-width="1"/>
</svg>

<!-- Reboot: all text -->
<section class="card col-1 row-1" style="background:var(--blush)">
  <svg class="shapes" viewBox="0 0 220 275" aria-hidden="true">
    <path d="M0 70 C40 20 140 10 220 0" fill="none" stroke="#fff" stroke-width="2"/>
    <path d="M150 275 C180 250 205 230 220 210" fill="none" stroke="#fff" stroke-width="1.5"/>
    <circle cx="110" cy="75" r="43" fill="var(--forest)"/>
  </svg>
  <div class="t script white" style="left:72px;top:40px;font-size:44px">21</div>
  <div class="t white" style="left:95px;top:84px;font-size:13px">NIGHT</div>
  <div class="t forest center" style="top:126px;font-size:18px">LEAN</div>
  <div class="t forest center" style="top:146px;font-size:30px;font-weight:900">MIDDLE</div>
  <div class="t rose center" style="top:180px;font-size:13px;padding-left:40px">REBOOT</div>
  <div class="t script rose center" style="top:192px;font-size:42px">Beyond 50</div>
</section>

<section class="card col-2 row-1" style="background:var(--rose)">
  <div class="photo" role="img" aria-label="Photo of smiling woman in cropped white sweater pointing at her waist in a kitchen" style="inset:0;background:linear-gradient(160deg,var(--photo-warm-a),var(--photo-warm-b))"></div>
  <svg class="shapes" viewBox="0 0 220 275" aria-hidden="true">
    <path d="M170 0 L220 0 L220 40 C200 30 185 15 170 0Z" fill="var(--rose)"/>
    <path d="M0 150 C20 150 20 175 45 180 C90 190 130 185 170 175 C200 165 215 150 220 140 L220 275 L0 275Z" fill="var(--rose)"/>
  </svg>
  <div class="t white" style="right:6px;top:16px;font-size:50px;font-weight:900">21</div>
  <div class="t forest" style="right:8px;top:66px;font-size:22px;font-weight:900">NIGHT</div>
  <div class="t white center" style="top:198px;font-size:22px;font-weight:900">LEAN MIDDLE</div>
  <div class="t forest" style="left:20px;top:244px;font-size:12px">REBOOT</div>
  <div class="t script white" style="left:82px;top:228px;font-size:32px">Beyond 50</div>
</section>

<section class="card col-3 row-1" style="background:var(--blush)">
  <svg class="shapes" viewBox="0 0 220 275" aria-hidden="true">
    <path d="M12 0 L220 0 L220 250 C190 255 150 250 120 245 C80 240 40 200 20 150 C0 90 10 40 12 0Z" fill="var(--rose)"/>
  </svg>
  <div class="photo" role="img" aria-label="Cutout photo of smiling woman in cropped white sweater and black pants pointing at her waist" style="left:5px;top:0;width:150px;height:275px;border-radius:45% 45% 0 0;background:linear-gradient(180deg,var(--photo-warm-b),#3a302c)"></div>
  <div class="t script white" style="right:18px;top:20px;font-size:42px">21</div>
  <div class="t forest" style="right:16px;top:60px;font-size:14px;font-weight:900">NIGHT</div>
  <div class="t forest" style="right:8px;top:88px;font-size:17px;font-weight:900">LEAN</div>
  <div class="t forest" style="right:6px;top:108px;font-size:25px;font-weight:900">MIDDLE</div>
  <div class="t white" style="right:26px;top:208px;font-size:11px">REBOOT</div>
  <div class="t script white" style="right:10px;top:218px;font-size:30px">Beyond 50</div>
</section>

<!-- Menu guide -->
<section class="card col-1 row-2" style="background:var(--forest)">
  <svg class="shapes" viewBox="0 0 220 275" aria-hidden="true">
    <path d="M0 95 C60 110 120 110 220 90 L220 180 C170 170 100 165 0 180Z" fill="var(--rose)"/>
  </svg>
  <div class="t rose center" style="top:35px;font-size:17px">THE</div>
  <div class="t script white" style="left:32px;top:52px;font-size:40px">20</div>
  <div class="t white" style="left:80px;top:71px;font-size:17px">SECOND</div>
  <div class="t white center" style="top:98px;font-size:38px;font-weight:900">TRIM-</div>
  <div class="t white center" style="top:142px;font-size:38px;font-weight:900">CORE</div>
  <div class="t script white center" style="top:190px;font-size:38px">Menu Guide</div>
</section>

<section class="card col-2 row-2" style="background:var(--rose)">
  <div class="photo" role="img" aria-label="Photo of meal plan notebook on dark wood with salmon, eggs, tomatoes, lentils and greens" style="inset:0;background:linear-gradient(135deg,var(--photo-food-a),var(--photo-food-b))"></div>
  <svg class="shapes" viewBox="0 0 220 275" aria-hidden="true">
    <path d="M20 0 L0 0 L0 275 L220 275 L220 0 L205 0 C215 40 200 70 205 110 C210 170 190 230 130 235 C90 238 80 180 45 165 C20 155 30 20 20 0Z" fill="var(--rose)"/>
    <path d="M0 150 C15 150 30 160 45 175 L60 275 L0 275Z" fill="var(--photo-food-b)" opacity=".6"/>
  </svg>
  <div class="t script white" style="left:38px;top:12px;font-size:42px">20</div>
  <div class="t white" style="left:96px;top:14px;font-size:16px">THE</div>
  <div class="t white" style="left:94px;top:32px;font-size:16px">SECOND</div>
  <div class="t script white" style="left:42px;top:226px;font-size:32px">Menu Guide</div>
</section>

<section class="card col-3 row-2" style="background:var(--rose)">
  <div class="photo" role="img" aria-label="Photo of meal plan sheet on wood surrounded by bowls of fruit, vegetables and yogurt" style="inset:0;background:linear-gradient(160deg,var(--photo-food-b),var(--photo-food-a))"></div>
  <svg class="shapes" viewBox="0 0 220 275" aria-hidden="true">
    <path d="M0 0 L220 0 L220 10 C150 20 80 15 0 20Z" fill="var(--rose)"/>
  </svg>
  <div class="t script white" style="left:34px;top:52px;font-size:42px">20</div>
  <div class="t white" style="left:108px;top:54px;font-size:16px">THE</div>
  <div class="t white" style="left:90px;top:72px;font-size:16px">SECOND</div>
  <div class="t white center" style="top:104px;font-size:26px;font-weight:900">TRIM-CORE</div>
</section>

<!-- Starlet tricks -->
<section class="card col-1 row-3" style="background:var(--blush)">
  <svg class="shapes" viewBox="0 0 220 275" aria-hidden="true">
    <path d="M0 100 C40 75 120 70 220 55" fill="none" stroke="#fff" stroke-width="1.5"/>
    <path d="M0 225 C60 195 130 190 220 205 L220 275 L0 275Z" fill="var(--rose)"/>
  </svg>
  <div class="t rose center" style="top:40px;font-size:23px;font-weight:900">STARLET</div>
  <div class="t forest center" style="top:70px;font-size:28px;font-weight:900">TRICKS</div>
  <div class="t forest center" style="top:107px;font-size:12px">TO A SLENDER MIDLINE</div>
  <div class="t script rose center" style="top:135px;font-size:44px">Beyond 50</div>
  <div class="t white center" style="top:247px;font-size:11px;font-weight:700">ZERO SCALPEL NEEDED</div>
</section>

<section class="card col-2 row-3" style="background:var(--rose)">
  <div class="photo" role="img" aria-label="Photo of one woman whispering a secret to another surprised woman" style="left:0;top:0;width:220px;height:212px;background:linear-gradient(135deg,#3a2a22,#c99a84)"></div>
  <div class="t white center" style="top:145px;font-size:29px;font-weight:900">STARLET</div>
  <div class="t white center" style="top:175px;font-size:29px;font-weight:900">TRICKS</div>
  <div class="t white" style="left:14px;top:222px;font-size:9px">TO A SLENDER MIDLINE</div>
  <div class="t script white" style="left:16px;top:234px;font-size:30px">Beyond 50</div>
  <div class="badge" style="left:160px;top:214px;width:52px;height:52px">
    <span style="font-size:11px;font-weight:900">ZERO</span>
    <span style="font-size:5px;font-weight:700;line-height:1.2">SCALPEL<br>NEEDED</span>
  </div>
</section>

<section class="card col-3 row-3" style="background:var(--rose)">
  <div class="photo" role="img" aria-label="Photo of one woman whispering to an excited woman against a blue backdrop" style="inset:0;background:var(--photo-sky)"></div>
  <svg class="shapes" viewBox="0 0 220 275" aria-hidden="true">
    <path d="M0 0 L60 0 C20 15 0 60 10 110 C20 150 50 165 90 170 C130 175 140 200 135 230 C130 255 110 270 120 275 L0 275Z" fill="var(--rose)"/>
  </svg>
  <div class="photo" role="img" aria-label="Photo detail of the two women's figures" style="left:120px;top:150px;width:100px;height:125px;background:linear-gradient(180deg,#c79a85,#2c4a78)"></div>
  <div class="t white" style="left:22px;top:168px;font-size:14px;font-weight:900">STARLET TRICKS</div>
  <div class="t white" style="left:26px;top:189px;font-size:8px;letter-spacing:3px">TO A</div>
  <div class="t white" style="left:24px;top:200px;font-size:12px">SLENDER MIDLINE</div>
  <div class="t script white" style="left:24px;top:214px;font-size:28px">Beyond 50</div>
  <div class="t forest" style="left:24px;top:252px;font-size:11px;font-weight:800">ZERO SCALPEL NEEDED</div>
</section>

</body>
</html>
```